Banner 34"x81"

This is for a Pull Up Banner
I am supplying a sample of my logo and some of my art work for you to incorporate into an upright banner.
Please business name:LuellaRo OpenHarbor Psychotherapy
phone number: 583-214-9067 NOT THE ONE ON THE BUSINESS CARD

```html
<!DOCTYPE html>
<html lang="en">
<head>
<meta charset="utf-8">
<title>LuellaRo OpenHarbor Psychotherapy – Pull Up Banner</title>
<link href="https://fonts.googleapis.com/css2?family=Pathway+Gothic+One&family=Russo+One&display=swap" rel="stylesheet">
<style>
  :root {
    --page-bg: #eceff1;
    --banner-white: #ffffff;
    --brand-blue: #2a54a3;
    --headline-blue: #16468c;
    --accent-red: #e53a35;
    --cream: #f6dcc4;
    --ink: #111111;
    --photo-dark: #2e2220;
    --photo-mid: #4a3a3c;
    --photo-blue: #3451a8;
  }
  * { margin: 0; padding: 0; box-sizing: border-box; }
  html, body { width: 1200px; height: 1200px; overflow: hidden; }
  body {
    background: var(--page-bg);
    position: relative;
    font-family: "Pathway Gothic One", "Arial Narrow", sans-serif;
  }
  .banner {
    position: absolute;
    left: 380px; top: 75px;
    width: 441px; height: 1050px;
    background: var(--banner-white);
    box-shadow: 0 2px 8px rgba(0,0,0,0.12);
  }
  .brand-panel {
    position: absolute;
    left: 0; top: 0;
    width: 100%; height: 450px;
    background: var(--brand-blue);
  }
  .brand-name, .brand-tagline {
    position: absolute;
    left: 0; width: 100%;
    text-align: center;
    color: var(--cream);
    line-height: 1;
  }
  .brand-name { top: 56px; font-size: 40px; }
  .brand-tagline { top: 372px; font-size: 28px; }
  .brand-square {
    position: absolute;
    left: 147px; top: 104px;
    width: 161px; height: 256px;
    border: 4px solid var(--accent-red);
  }
  .portrait {
    position: absolute;
    left: 136px; top: 462px;
    width: 169px; height: 254px;
    background:
      radial-gradient(ellipse 45% 30% at 50% 72%, var(--photo-blue) 0%, rgba(52,81,168,0) 100%),
      linear-gradient(180deg, var(--photo-mid) 0%, var(--photo-dark) 100%);
  }
  .practice-name {
    position: absolute;
    left: 0; top: 730px; width: 100%;
    text-align: center;
    font-size: 37px;
    color: var(--ink);
    line-height: 1;
  }
  .practice-type {
    position: absolute;
    left: 0; top: 774px; width: 100%;
    text-align: center;
    font-family: "Russo One", "Arial Black", sans-serif;
    font-size: 44px;
    color: var(--headline-blue);
    line-height: 1;
    letter-spacing: 0.5px;
  }
  .contact-icons {
    position: absolute;
    left: 0; top: 856px; width: 100%;
    height: 34px;
  }
  .phone {
    position: absolute;
    left: 0; top: 910px; width: 100%;
    text-align: center;
    font-size: 34px;
    color: var(--ink);
    line-height: 1;
  }
  .handle {
    position: absolute;
    left: 0; width: 100%;
    text-align: center;
    font-size: 21px;
    color: var(--ink);
    line-height: 1;
  }
  .handle--primary { top: 953px; }
  .handle--secondary { top: 983px; }
</style>
</head>
<body>
  <main class="banner">
    <section class="brand-panel">
      <p class="brand-name">Luella Ro</p>
      <div class="brand-square"></div>
      <p class="brand-tagline">Open Harbor</p>
    </section>

    <div class="portrait" role="img" aria-label="Portrait photo of the therapist seated on a dark leather sofa"></div>

    <h1 class="practice-name">LuellaRo OpenHarbor</h1>
    <h2 class="practice-type">PSYCHOTHERAPY</h2>

    <svg class="contact-icons" width="441" height="34" viewBox="0 0 441 34" aria-hidden="true">
      <g class="icon-phone">
        <circle cx="171" cy="17" r="16" fill="var(--accent-red)"/>
        <path d="M165 10 q-2 1 -1.5 4 q2 7 9 10 q3 1 4 -1 l1 -1.5 -3.5 -2.5 -1.7 1.6 q-3 -1.5 -4.5 -4.5 l1.6 -1.7 -2.5 -3.5 z" fill="#ffffff"/>
      </g>
      <circle class="icon-social" cx="221" cy="17" r="16" fill="var(--accent-red)"/>
      <circle class="icon-social" cx="269" cy="17" r="16" fill="var(--accent-red)"/>
    </svg>

    <p class="phone">583-214-9067</p>
    <p class="handle handle--primary">@luellaopenHarbor</p>
    <p class="handle handle--secondary">@luellaopen</p>
  </main>
</body>
</html>
```